Brightfold Systems, a software development company, needs a website

We need a website to promote our software development company. The company is brand new and we want to market ourselves. We develop all kinds of software from web applications, to desktop applications, to mobile applications. Small company, not a lot of history, just need something flashy.

```html
<!DOCTYPE html>
<html lang="en">
<head>
<meta charset="utf-8">
<title>Brightfold Systems</title>
<link href="https://fonts.googleapis.com/css2?family=Nunito:wght@400;600&family=Ubuntu:wght@400;500&display=swap" rel="stylesheet">
<style>
:root{
  --red:#dc3545;
  --bright-red:#ff0000;
  --blue:#0000ff;
  --link:#007bff;
  --ink:#212529;
  --muted-bg:#f8f9fa;
  --white:#ffffff;
  --rule:#e3e3e3;
}
*{box-sizing:border-box;margin:0;padding:0}
html,body{width:1200px;height:2501px;overflow:hidden;background:var(--white)}
body{position:relative;font-family:"Nunito",sans-serif;color:var(--ink);font-size:16px}
.abs{position:absolute}
h1,h2,h3,h4,.heading{font-family:"Ubuntu",sans-serif;font-weight:500}

.navbar{left:0;top:0;width:1200px;height:59px;background:var(--muted-bg)}
.brand-small{left:20px;top:17px;font-size:20px}
.brand-small .a{color:var(--blue)}
.brand-small .b{color:var(--bright-red)}
.nav-links{right:30px;top:19px;display:flex;gap:17px;font-size:16px}

.hero{left:12px;top:59px;width:1168px;height:632px;background:linear-gradient(120deg,#6d6c70 0%,#5c5b60 45%,#3a393d 70%,#55545a 100%)}
.hero-line{left:186px;color:var(--white);font-size:42px;font-family:"Ubuntu",sans-serif;font-weight:500}
.hero-line .mark{background:var(--red);padding:6px 6px}

.section-title{left:0;width:1200px;text-align:center;font-size:39px;color:var(--ink)}
.service{width:380px;text-align:center}
.service svg{display:block;margin:0 auto}
.service h3{font-size:21px;margin-top:2px}
.service p{font-size:16px;line-height:25px;margin-top:10px;padding:0 20px}

.overview{left:8px;top:950px;width:1172px;height:261px;background:var(--muted-bg)}
.centered-text{left:0;width:1200px;text-align:center;font-size:16px;line-height:25px}
.btn-red{left:506px;top:1127px;width:174px;height:69px;background:var(--bright-red);color:var(--white);font-size:31px;text-align:center;line-height:69px;border-radius:3px}

.work-card{width:380px}
.work-photo{width:379px;height:282px}
.work-card h3{font-size:29px;line-height:31px;margin-top:4px;padding-right:20px}
.work-card p{font-size:16px;line-height:25.3px;margin-top:10px;padding-right:30px}
.work-card .more{display:block;color:var(--bright-red);margin-top:17px}

.cta{left:4px;top:1999px;width:1195px;height:125px;background:var(--red)}
.cta-text{left:9px;top:2027px;color:var(--white);font-size:31px}
.cta-btn{left:994px;top:2024px;width:199px;height:74px;border:1px solid var(--white);color:var(--white);font-size:31px;text-align:center;line-height:72px}

.footer-brand{left:34px;top:2165px;font-size:42px;font-family:"Ubuntu",sans-serif;font-weight:500}
.footer-brand .a{color:var(--blue)}
.footer-brand .b{color:var(--bright-red)}
.footer-about{left:34px;top:2221px;width:520px;font-size:16px;line-height:25.3px}
.footer-more{left:34px;top:2366px;color:var(--link)}
.footer-head{font-size:25px;font-family:"Ubuntu",sans-serif;font-weight:500}
.links{left:609px;top:2163px}
.links ol{margin-top:8px;padding-left:24px;font-size:16px;line-height:25.3px}
.links li{color:var(--ink)}
.links li span{color:var(--link)}
.contact{left:800px;top:2163px;width:260px;font-size:16px;line-height:25.3px}
.contact p{margin-top:10px}
.rule{left:0;top:2415px;width:1200px;height:1px;background:var(--rule)}
.copyright{left:34px;top:2443px;font-size:16px}
.social{left:896px;top:2446px;display:flex;gap:19px;align-items:center}
</style>
</head>
<body>

<header class="navbar abs">
  <div class="brand-small abs"><span class="a">Brightfold</span> <span class="b">systems</span></div>
  <nav class="nav-links abs"><span>Home</span><span>Services</span><span>Solutions</span><span>About</span><span>Contact</span></nav>
</header>

<section class="hero abs" role="img" aria-label="Designer pinning photographs to a white brick wall, darkened overlay"></section>
<div class="hero-line abs" style="top:286px">We’re an Independent software</div>
<div class="hero-line abs" style="top:384px">Design and <span class="mark">Development</span></div>
<div class="hero-line abs" style="top:482px">Agency.</div>

<h2 class="section-title abs" style="top:718px">Our services</h2>
<div class="service abs" style="left:3px;top:774px">
  <svg width="44" height="48" viewBox="0 0 44 48"><rect x="4" y="0" width="36" height="48" rx="14" fill="var(--bright-red)"/><rect x="13" y="7" width="18" height="34" rx="4" fill="var(--white)"/><rect x="16" y="10" width="12" height="24" fill="var(--bright-red)"/></svg>
  <h3>Mobile Application</h3>
  <p>Lorem ipsum dolor sit amet, consectetur adipisicing elit. Nemo, culpa!</p>
</div>
<div class="service abs" style="left:403px;top:774px">
  <svg width="60" height="48" viewBox="0 0 60 48"><ellipse cx="30" cy="24" rx="30" ry="24" fill="var(--bright-red)"/><rect x="17" y="11" width="26" height="18" rx="2" fill="var(--white)"/><rect x="20" y="14" width="20" height="12" fill="var(--bright-red)"/><rect x="12" y="31" width="36" height="5" rx="2" fill="var(--white)"/></svg>
  <h3>Web Application</h3>
  <p>Lorem ipsum dolor sit amet, consectetur adipisicing elit. Nemo, culpa!</p>
</div>
<div class="service abs" style="left:803px;top:774px">
  <svg width="54" height="48" viewBox="0 0 54 48"><ellipse cx="27" cy="24" rx="27" ry="24" fill="var(--bright-red)"/><rect x="13" y="11" width="28" height="19" rx="2" fill="var(--white)"/><rect x="16" y="14" width="22" height="13" fill="var(--bright-red)"/><rect x="24" y="30" width="6" height="4" fill="var(--white)"/><rect x="19" y="34" width="16" height="3" rx="1" fill="var(--white)"/></svg>
  <h3>Desktop application</h3>
  <p>Lorem ipsum dolor sit amet, consectetur adipisicing elit. Nemo, culpa!</p>
</div>

<section class="overview abs"></section>
<h2 class="section-title abs" style="top:980px">Company Overview</h2>
<p class="centered-text abs" style="top:1035px">Lorem ipsum dolor sit amet, consectetur adipisicing elit. Quibusdam laboriosam eum, minus,<br>aliquam, suscipit totam aspernatur labore vero maxime quas quam aperiam ea ullam.<br>Eaque voluptate porro numquam illo laborum.</p>
<div class="btn-red abs">View More</div>

<h2 class="section-title abs" style="top:1241px">Our work expierence</h2>
<p class="centered-text abs" style="top:1296px">Lorem ipsum dolor sit amet, consectetur adipisicing elit. Quibusdam laboriosam eum, minus,<br>aliquam, suscipit totam aspernatur labore vero maxime quas quam aperiam ea ullam.<br>Eaque voluptate porro numquam illo laborum.</p>

<article class="work-card abs" style="left:10px;top:1388px">
  <div class="work-photo" role="img" aria-label="Open laptop on a wooden desk" style="background:linear-gradient(135deg,#c98a55 0%,#e6d5c4 45%,#9a9fa6 100%)"></div>
  <h3>Lorem ipsum dolor sit amet, consectetur adipisicing elit.</h3>
  <p>Lorem ipsum dolor sit amet, consectetur adipisicing elit. Hic, dolorem rerum exercitationem, autem nemo cupiditate, dignissimos dolores aperiam rem perferendis cumque sit, voluptates asperiores excepturi laborum officia ut nobis repellat.</p>
  <span class="more">Read More</span>
</article>
<article class="work-card abs" style="left:410px;top:1388px">
  <div class="work-photo" role="img" aria-label="Hands resting beside laptops on an office desk" style="background:linear-gradient(135deg,#4d4a52 0%,#c9c7c4 50%,#ebe8e3 100%)"></div>
  <h3>Lorem ipsum dolor sit amet, consectetur adipisicing elit.</h3>
  <p>Lorem ipsum dolor sit amet, consectetur adipisicing elit. Hic, dolorem rerum exercitationem, autem nemo cupiditate, dignissimos dolores aperiam rem perferendis cumque sit, voluptates asperiores excepturi laborum officia ut nobis repellat.</p>
  <span class="more">Read More</span>
</article>
<article class="work-card abs" style="left:810px;top:1390px">
  <div class="work-photo" role="img" aria-label="Desktop monitors, keyboard and coffee mug on a white desk" style="background:linear-gradient(160deg,#1c2130 0%,#3d4150 40%,#e7e7e7 75%,#f2f2f2 100%)"></div>
  <h3>Lorem ipsum dolor sit amet, consectetur adipisicing elit.</h3>
  <p>Lorem ipsum dolor sit amet, consectetur adipisicing elit. Hic, dolorem rerum exercitationem, autem nemo cupiditate, dignissimos dolores aperiam rem perferendis cumque sit, voluptates asperiores excepturi laborum officia ut nobis repellat.</p>
  <span class="more">Read More</span>
</article>

<section class="cta abs"></section>
<div class="cta-text abs">You think we're cool? let's work together</div>
<div class="cta-btn abs">Contact us</div>

<div class="footer-brand abs"><span class="a">Brightfold</span><span class="b">Systems</span></div>
<p class="footer-about abs">Lorem ipsum dolor sit amet, consectetur adipisicing elit. Maxime accusamus mollitia dicta enim vel velit, animi, assumenda perferendis fugit quos corporis architecto distinctio recusandae esse voluptatem nobis eligendi. Modi omnis aliquam doloribus natus, necessitatibus rerum, repudiandae maiores deserunt voluptatum minus.</p>
<span class="footer-more abs">Read More</span>

<div class="links abs">
  <h4 class="footer-head">Helpful-links</h4>
  <ol><li><span>lorem ispum</span></li><li><span>lorem ispum</span></li><li><span>lorem ispum</span></li><li><span>lorem ispum</span></li><li><span>lorem ispum</span></li></ol>
</div>
<div class="contact abs">
  <h4 class="footer-head">Contact Us</h4>
  <p style="margin-top:8px">2210 Harlow Lane Near Mill Park, U.S</p>
  <p>Phone: 014-55501234</p>
  <p>Email: info@brightfoldsystems.org</p>
</div>

<div class="rule abs"></div>
<div class="copyright abs">COPYRIGHT 2017 Brightfold Systems inc. | ALL RIGHTS RESERVED</div>
<div class="social abs" aria-label="Social links">
  <svg width="16" height="16" viewBox="0 0 16 16"><rect width="16" height="16" rx="2" fill="var(--ink)"/></svg>
  <svg width="16" height="16" viewBox="0 0 16 16"><circle cx="8" cy="8" r="7" fill="none" stroke="var(--ink)" stroke-width="2"/></svg>
  <svg width="18" height="18" viewBox="0 0 24 24"><path d="M6.6 10.8a15 15 0 0 0 6.6 6.6l2.2-2.2c.3-.3.7-.4 1-.2 1.1.4 2.3.6 3.6.6.6 0 1 .4 1 1V20c0 .6-.4 1-1 1A17 17 0 0 1 3 4c0-.6.4-1 1-1h3.5c.6 0 1 .4 1 1 0 1.3.2 2.5.6 3.6.1.3 0 .7-.2 1z" fill="var(--ink)" transform="scale(-1,1) translate(-24,0)"/></svg>
  <svg width="16" height="16" viewBox="0 0 16 16"><circle cx="8" cy="8" r="8" fill="var(--ink)"/></svg>
</div>

</body>
</html>
```